Body corporate management needs business principle flyer design

We need a one page A4 flyer design for our business principles.
We manage body corporates and strata properties.
Brightwick is a new initiative for our company. Its a label that we have given to our principles of business that drive our people, systems and processes to give assurance to our clients that every detail matters.
We would like to be able to include this design in future brochure so we are after 1 x portrait and 1 x landscape.
The design needs to portray professionalism.
We would like to see designs that use the colour red. (see attached logo).

Target Market(s)

Professionals

Industry/Entity Type

Business

Font styles to use
Sans Serif

Requirements
Must have
• Brightwick logo, provide the design file and as pdf
Nice to have
• the use of the colour red from the logo

```html
<!DOCTYPE html>
<html lang="en">
<head>
<meta charset="utf-8">
<title>Brightwick – Principles of Business</title>
<link href="https://fonts.googleapis.com/css2?family=Mulish:wght@400;700&family=Didact+Gothic&display=swap" rel="stylesheet">
<style>
  :root {
    --brand-red: #d42a27;
    --deep-red: #9e0f0f;
    --panel-dark: #4f7f95;
    --panel-light: #b4cdd8;
    --steel: #7fa3b5;
    --steel-light: #c3d6df;
    --ink: #151a1d;
    --paper: #ffffff;
  }
  * { margin: 0; padding: 0; box-sizing: border-box; }
  html, body { width: 907px; height: 1200px; overflow: hidden; background: var(--paper); }
  .flyer { position: relative; width: 907px; height: 1200px; font-family: "Mulish", sans-serif; }
  .flyer-shapes { position: absolute; inset: 0; }
  .brand-name {
    position: absolute; left: 38px; top: 104px;
    font-family: "Didact Gothic", sans-serif; font-size: 46px; font-weight: 400;
    color: var(--brand-red); letter-spacing: 0.5px;
  }
  .intro-panel {
    position: absolute; left: 314px; top: 22px; width: 570px; height: 284px;
    border-radius: 10px;
    background: linear-gradient(100deg, var(--panel-dark) 0%, #7ea3b4 55%, var(--panel-light) 100%);
    padding: 14px 16px 12px 14px; color: var(--ink);
  }
  .intro-lead { font-weight: 700; font-size: 16.5px; line-height: 1.2; margin-bottom: 14px; text-align: justify; }
  .principle h3 { font-size: 15px; font-weight: 700; line-height: 1.15; }
  .principle p { font-size: 13px; line-height: 16.5px; text-align: justify; }
  .intro-panel .principle p { font-size: 13.6px; line-height: 16px; }
  .intro-panel .principle { margin-bottom: 10px; }
  .principles-list {
    position: absolute; left: 28px; top: 606px; width: 850px; color: var(--paper);
  }
  .principles-list .principle { margin-bottom: 6px; }
  .principles-list .narrow-1 { width: 545px; }
  .principles-list .narrow-2 { width: 710px; }
  .principles-list .narrow-1 p, .principles-list .narrow-2 p { text-align: left; }
</style>
</head>
<body>
<div class="flyer">
  <svg class="flyer-shapes" width="907" height="1200" viewBox="0 0 907 1200" aria-hidden="true">
    <defs>
      <linearGradient id="photoTone" x1="0" y1="0" x2="1" y2="1">
        <stop offset="0" stop-color="#1f3f78"/>
        <stop offset="0.3" stop-color="#5a7fb0"/>
        <stop offset="0.6" stop-color="#9fb6d6"/>
        <stop offset="1" stop-color="#d6e1ee"/>
      </linearGradient>
      <linearGradient id="redField" x1="0" y1="0" x2="1" y2="0.3">
        <stop offset="0" stop-color="var(--deep-red)"/>
        <stop offset="0.45" stop-color="var(--brand-red)"/>
        <stop offset="1" stop-color="#b8120f"/>
      </linearGradient>
      <linearGradient id="steelBand" x1="0" y1="0" x2="1" y2="0">
        <stop offset="0" stop-color="var(--steel)"/>
        <stop offset="0.5" stop-color="var(--steel-light)"/>
        <stop offset="1" stop-color="var(--steel)"/>
      </linearGradient>
    </defs>
    <rect class="handshake-photo" role="img" aria-label="Photo of a business handshake in front of glass office towers" x="0" y="280" width="907" height="480" fill="url(#photoTone)"/>
    <path class="top-white" d="M0 0 H907 V290 C700 320 480 345 300 338 C150 332 60 318 0 304 Z" fill="var(--paper)"/>
    <path class="red-swoosh" d="M0 160 C120 232 300 298 480 304 C650 308 800 282 907 262 V300 C700 332 500 346 300 340 C150 334 60 320 0 305 Z" fill="url(#redField)"/>
    <path class="steel-swoosh" d="M0 565 C320 545 650 560 907 700 V752 C660 595 320 572 0 590 Z" fill="url(#steelBand)"/>
    <path class="red-field" d="M0 590 C320 572 660 595 907 752 V1152 H0 Z" fill="url(#redField)"/>
    <rect class="base-band" x="0" y="1150" width="907" height="50" fill="url(#steelBand)"/>
  </svg>

  <div class="brand-name">Brightwick</div>

  <section class="intro-panel">
    <p class="intro-lead">Brightwick is our principles of business that drive our people, systems and processes to give assurance to our clients that every detail matters.</p>
    <div class="principle">
      <h3>1.&nbsp; Client Experience</h3>
      <p>Our promise is to pursue excellence and to continually deliver a solutions based service. We achieve this through active engagement, open channels of communication and a serviced led team with the dedicated resources to listen, engage and implement.</p>
    </div>
    <div class="principle">
      <h3>2.&nbsp; Loyalty</h3>
      <p>We seek to develop a life-time relationship with our clients, building trust by acting with integrity, honesty and courtesy. We achieve this due to our expert approach to strata management and providing a responsive service to our clients.</p>
    </div>
  </section>

  <section class="principles-list">
    <div class="principle narrow-1">
      <h3>3.&nbsp; Education and Guidance</h3>
      <p>We endeavor to always be proactive in client education and guidance. This is achieved by our internal and external communications, comprehensive training programs and cross-departmental collaboration of knowledge sharing.</p>
    </div>
    <div class="principle narrow-2">
      <h3>4.&nbsp; Compliance and Governance</h3>
      <p>We engage and own a position of ‘every detail matters’. We give due diligence to the relevant state and national legislations with which we, our clients and our stakeholders must comply. We regulate and achieve this through a robust system of internal processes and protocols which structure and confirm our deliverables are in line with regulations.</p>
    </div>
    <div class="principle">
      <h3>5.&nbsp; Systems and processes</h3>
      <p>We strive to be the best in our field, by implementing efficiencies without compromising service quality, accuracy or compliance. We continually seek to achieve this by reviewing, updating and adopting continuous improvement strategies, systems and quality processes that deliver outcomes.</p>
    </div>
    <div class="principle">
      <h3>6.&nbsp; Quality and Commitment</h3>
      <p>We invest in the recruitment and retention of a quality and diverse team of experienced professionals with a strong focus on continual professional development. As committed and skilled individuals, we actively promote the cross-departmental collaboration with one another to deliver a well rounded offering.</p>
    </div>
    <div class="principle">
      <h3>7.&nbsp; Delivery</h3>
      <p>We empower our teams to deliver an outstanding client service and to be accountable for their actions. We will make sure every detail matters, provide valuable insight and supply information in a clear and timely manner.</p>
    </div>
    <div class="principle">
      <h3>8.&nbsp; Integrity</h3>
      <p>Our approach to strata management is bound by honesty and a strong set of moral principles. We act in our clients’ best interests with diligence and transparency for understanding and accountability.</p>
    </div>
    <div class="principle">
      <h3>9.&nbsp; Continuous Improvement</h3>
      <p>Our goal is to continually evolve to better our offering and to be adaptable and responsive to change. Our infrastructure supports us to continually mould into the business that is right for our clients.</p>
    </div>
    <div class="principle">
      <h3>10. Ethical Stance</h3>
      <p>We aim to create a community of ethical business relationships where we contribute our values and services to give our clients outstanding reassurance of our abilities.</p>
    </div>
  </section>
</div>
</body>
</html>
```